Packaging & Label Design for CDB Products

We are a European CBD company specialising in athletic recovery, sleep improvement and wellness.

We would like the packaging to incorporate our logo and name (and font 'Codec') 'Lanternfield CBD'. The design must be transferable to all of our products. CBD Oils, Balms, Lip Balm and Vape E-Liquid.

We would like it to be simple but eye-catching and modern. We don't want bright colours. Preferred pallet of muted greys, blacks, white and pastel colours. Geometric concepts, possibly using different colours for each item of the range, we are open to new and fresh ideas (we are seeking you for your experience) and when we find the right design we would likely throw more work in your direction..

Our product range is not complete so the designer must be flexible with some changes and provide files where format can be easily edited by packaging manufacturer. We are also waiting for dimensions for the labels and boxes for several products and will supply the designer with full dimensions of all products once selected.

Oil Box: 2.6 x 9.0 x 2.6 cm (open format 16.7 x 11.6cm)
Labels: 7.8 x 3.3 cm (Front and Back)

Our expected product range will be:
CBD Oil 1000mg
CBD Oil 3000mg
CBD Balm 100mg
CBD Balm 300mg
E-Liquid 500mg
Lip Balm 50mg

We look forward to seeing your ideas.

Best Regards
Lanternfield CBD

```html
<!DOCTYPE html>
<html lang="en">
<head>
<meta charset="utf-8">
<title>Lanternfield CBD – CBD Oil 1000mg Label</title>
<link href="https://fonts.googleapis.com/css2?family=Montserrat:wght@400;500;600;700&display=swap" rel="stylesheet">
<style>
  :root {
    --lavender: #bc97da;
    --lavender-deep: #9a6cc6;
    --ink: #2b2b2b;
    --charcoal: #3a3a3a;
    --paper-top: #fbfbfb;
    --paper-bottom: #e9e9e9;
    --stage: #f2f2f2;
    --flag-blue: #2a3f7a;
  }
  * { box-sizing: border-box; margin: 0; padding: 0; }
  html, body { width: 1200px; height: 900px; overflow: hidden; }
  body {
    background: var(--stage);
    font-family: "Montserrat", sans-serif;
    color: var(--ink);
    position: relative;
  }
  .label {
    position: absolute;
    left: 50px; top: 217px;
    width: 1100px; height: 466px;
    background: linear-gradient(180deg, var(--paper-top), var(--paper-bottom));
    overflow: hidden;
  }
  .label__band {
    position: absolute; left: 0; top: 0;
    width: 100%; height: 182px;
    background: var(--lavender);
  }
  .label__base-line {
    position: absolute; left: 0; bottom: 0;
    width: 100%; height: 10px;
    background: var(--charcoal);
  }
  .text-block { position: absolute; font-size: 18px; line-height: 19.5px; letter-spacing: -0.2px; }
  .text-block h3 { font-size: 18px; font-weight: 700; text-transform: uppercase; line-height: 20px; }
  .ingredients { left: 36px; top: 58px; width: 320px; }
  .directions { left: 36px; top: 200px; width: 320px; }
  .flag {
    position: absolute; left: 36px; top: 378px;
    width: 62px; height: 39px;
    background: var(--flag-blue);
  }
  .brand {
    position: absolute; left: 400px; top: 40px; width: 290px;
    text-align: center;
  }
  .brand__mark {
    width: 40px; height: 40px; border-radius: 50%;
    background: var(--charcoal); margin: 0 auto 14px;
  }
  .brand__name {
    font-size: 19px; font-weight: 700; letter-spacing: 1px;
    text-transform: uppercase; color: var(--charcoal);
  }
  .product-box {
    position: absolute; left: 447px; top: 157px; width: 193px;
    border: 2px solid var(--charcoal); background: #fff;
  }
  .product-box__title {
    color: var(--lavender-deep); font-weight: 400;
    font-size: 36px; line-height: 34px; letter-spacing: -0.5px;
    padding: 10px 8px 6px; text-transform: uppercase;
  }
  .product-box__sub {
    border-top: 2px solid var(--charcoal);
    font-size: 17px; font-weight: 600; line-height: 21px;
    text-align: center; padding: 2px 0 3px; text-transform: uppercase;
  }
  .variant {
    position: absolute; left: 450px; top: 337px; width: 190px; height: 32px;
    background: var(--lavender); color: var(--charcoal);
    font-size: 19px; font-weight: 500; letter-spacing: 12px;
    text-align: center; line-height: 32px; padding-left: 12px;
  }
  .volume {
    position: absolute; left: 447px; top: 422px; width: 196px; height: 44px;
    background: linear-gradient(180deg, var(--paper-top), var(--paper-bottom));
    border-left: 2px solid var(--charcoal); border-right: 2px solid var(--charcoal);
    font-size: 22px; letter-spacing: -0.8px; text-align: center; line-height: 34px;
  }
  .caution {
    position: absolute; left: 757px; top: 32px; width: 303px; height: 218px;
    border: 3px solid var(--charcoal); background: #fff;
    padding: 4px 10px; text-align: center;
    font-size: 16.5px; line-height: 18.5px; letter-spacing: -0.8px;
  }
  .caution h3 { font-size: 21px; font-weight: 700; letter-spacing: -0.5px; line-height: 24px; text-transform: uppercase; }
  .caution p { text-align: justify; text-align-last: center; }
  .manufacturer { left: 757px; top: 274px; width: 320px; font-size: 19px; line-height: 23px; }
  .manufacturer h3 { font-size: 19px; }
  .contact { left: 757px; top: 368px; width: 320px; font-size: 19px; line-height: 24px; }
  .contact__handle { display: flex; align-items: center; gap: 6px; }
  .contact__square { width: 15px; height: 15px; background: var(--charcoal); border-radius: 2px; }
</style>
</head>
<body>
  <section class="label" aria-label="CBD Oil 1000mg label, front and back">
    <div class="label__band"></div>

    <div class="text-block ingredients">
      <h3>Ingredients:</h3>
      <p>Hemp Seed Oil, Omega-6 (2800mg), Omega-3 (930mg), CBD (1000mg) - 1 mg/drop</p>
    </div>

    <div class="text-block directions">
      <h3>Directions:</h3>
      <p>Food Supplement. Shake well before use. Use 4-6 drops 2-3 times a day. Leave the oil in your mouth for 30-60 seconds before swallowing. Gradually build up the dose to find your optimum dosage.</p>
    </div>

    <div class="flag" role="img" aria-label="Country of origin flag"></div>

    <div class="brand">
      <div class="brand__mark"></div>
      <div class="brand__name">Lanternfield CBD</div>
    </div>

    <div class="product-box">
      <div class="product-box__title">CBD Oil<br>1000mg</div>
      <div class="product-box__sub">Full Spectrum<br>Hemp Extract</div>
    </div>

    <div class="variant">RELAX</div>

    <div class="volume">1 Fl. oz. (30mL)</div>

    <div class="caution">
      <h3>Caution:</h3>
      <p>Do not exceed the recommended daily intake. Do not use as a substitute for a varied diet.</p>
      <p>Do not use during pregnancy and breastfeeding. Store in a dark and cool place, away from sunlight. Keep away from children.</p>
    </div>

    <div class="text-block manufacturer">
      <h3>Manufactured:</h3>
      <p>Lanternfield CBD Ltd, 18<br>Orchard Row, Harrow, HA2 7QD</p>
    </div>

    <div class="text-block contact">
      <p>www.lanternfield-cbd.com</p>
      <p class="contact__handle"><span class="contact__square"></span>@lanternfieldcbd</p>
    </div>

    <div class="label__base-line"></div>
  </section>
</body>
</html>
```